LeadTrim brochure design

I would like a brochure designed for our Leadtrim program.

LeadTrim is QBR’s flagship fitness program that combines exercise, nutrition, coaching tailored specifically to an executives’ lifestyle and customized specifically for them. LeadTrim is designed exclusively for C-level and senior executives in the top three tiers of the organization.

The brochure should contain pertinent info such as the services offered by leadtrim, (http://www.quartzbridgerehab.example/leadtrim-services), as well as some of the other benefits of LeadTrim program. All of the information can be gleaned from our LeadTrim pages (http://www.quartzbridgerehab.example/leadtrim). Also, I would like to incorporate the pull phrase under the WHY LEADTRIM heading on that webpage.

I would also like to see graphics used from our website banner (http://www.quartzbridgerehab.example/corporate-fitness)

All the details can be pulled from our website http://www.quartzbridgerehab.example/leadtrim

Target Market(s)

Senior and C-Level executives in large to midsize companies. Owners of smaller companies.

Industry/Entity Type

Fitness

Requirements
Must have
• The brochure must use our logo (attached) It should be consistent with the look of our other brochures (please see attached detox brochure) or consistent with our build your armor and faster art work (please see attached).
• It must be a tri-fold. It must have some artwork. The artwork should represent fitness for a business person. Picvault has great images (keyword: suit, dumbbell).
Nice to have
• May be nice to have a pic of our facility and possibly a pic of me the owner. Please see attached.

```html
<!DOCTYPE html>
<html lang="en">
<head>
<meta charset="utf-8">
<title>LeadTrim Tri-fold Brochure</title>
<link rel="stylesheet" href="https://fonts.googleapis.com/css2?family=PT+Sans:wght@400;700&display=swap">
<style>
  :root {
    --page-bg: #e9e6e1;
    --panel-grey: #b7b5b6;
    --pill-grey: #dddcdd;
    --story-grey: #cfcecf;
    --charcoal: #353535;
    --ink: #1b1b1b;
    --black: #0c0c0c;
    --white: #ffffff;
    --rule: #d8d8d8;
    --banner-blue: #2f4f73;
    --logo-grey: #8d8d8d;
    --mark-light: #e2e2e2;
  }
  * { box-sizing: border-box; margin: 0; padding: 0; }
  html, body { width: 1200px; height: 890px; overflow: hidden; }
  body {
    background: var(--page-bg);
    font-family: "PT Sans", "Helvetica Neue", Arial, sans-serif;
    color: var(--ink);
    position: relative;
  }
  .brochure {
    position: absolute; left: 60px; top: 46px; width: 1082px; height: 838px;
    background: var(--panel-grey);
  }
  .brochure > * { position: absolute; }
  .top-bar { left: 0; top: 0; width: 1082px; height: 12px; background: var(--black); }
  .foot-band { left: 0; top: 682px; width: 1082px; height: 142px; background: var(--charcoal); }
  .foot-bar { left: 0; top: 824px; width: 1082px; height: 14px; background: var(--black); }

  /* back panel */
  .banner {
    left: 2px; top: 12px; width: 360px; height: 95px;
    background: linear-gradient(90deg, #ffffff 0%, #f3f3f3 55%, #c9c9c9 78%, #f5f5f5 100%);
  }
  .banner-kicker { left: 14px; top: 42px; font-size: 6.5px; letter-spacing: .3px; color: var(--ink); text-transform: uppercase; }
  .banner-title { left: 12px; top: 48px; font-size: 23px; letter-spacing: -.5px; color: var(--banner-blue); }
  .banner-tag {
    left: 0; top: 74px; width: 222px; height: 22px; background: var(--black); color: var(--white);
    border-radius: 0 12px 12px 0; font-size: 7.5px; line-height: 9px; padding: 2px 0 0 12px;
  }
  .pill {
    background: var(--pill-grey); border-radius: 12px; text-align: center;
    font-weight: 700; color: var(--ink);
  }
  .pill-corporate { left: 41px; top: 126px; width: 282px; height: 47px; font-size: 22px; line-height: 47px; }
  .body-copy { font-size: 14px; line-height: 19.1px; text-align: justify; hyphens: auto; }
  .copy-corporate { left: 28px; top: 191px; width: 313px; }
  .photo-team {
    left: 34px; top: 384px; width: 296px; height: 160px; border-radius: 14px;
    background: linear-gradient(135deg, #f1eee6 0%, #d9c6a8 40%, #b9a06e 70%, #eae4d6 100%);
  }
  .brand-name {
    left: 60px; top: 618px; width: 250px; text-align: center;
    font-size: 20px; font-weight: 700; letter-spacing: 1px; color: var(--logo-grey);
  }
  .service-list { list-style: none; color: var(--white); font-size: 14px; line-height: 22px; }
  .service-list li::before { content: "\2022"; margin-right: 8px; }
  .list-back { left: 18px; top: 708px; }

  /* inside panel */
  .pill-leadtrim { left: 483px; top: 27px; width: 110px; height: 43px; font-size: 22px; line-height: 43px; }
  .copy-leadtrim { left: 382px; top: 86px; width: 320px; }
  .services-box {
    left: 384px; top: 377px; width: 316px; height: 305px; background: var(--charcoal);
    border-radius: 14px 14px 0 0; color: var(--white);
  }
  .services-title {
    position: absolute; left: 74px; top: 16px; width: 176px; text-align: center;
    font-size: 21px; font-weight: 700; padding-bottom: 2px; border-bottom: 1px solid var(--rule);
  }
  .services-copy { position: absolute; left: 9px; top: 66px; width: 300px; font-size: 13.5px; line-height: 19.2px; text-align: justify; }
  .services-rule { position: absolute; left: 66px; top: 284px; width: 183px; border-top: 1px solid var(--rule); }
  .list-inside { left: 456px; top: 708px; }

  /* front panel */
  .logo-card {
    left: 762px; top: 2px; width: 280px; height: 184px; background: var(--white);
    box-shadow: 2px 2px 3px rgba(0,0,0,.35);
    display: flex; align-items: center; justify-content: center; text-align: center;
  }
  .logo-card span { font-size: 26px; font-weight: 700; letter-spacing: 2px; color: var(--logo-grey); line-height: 1.2; }
  .story {
    left: 727px; top: 206px; width: 355px; height: 238px; background: var(--story-grey);
    padding: 8px 10px 0 9px; font-size: 14px; line-height: 19.1px; text-align: justify;
  }
  .photo-lift {
    left: 733px; top: 468px; width: 349px; height: 196px; box-shadow: 2px 2px 4px rgba(0,0,0,.4);
    background: linear-gradient(100deg, #5d5a55 0%, #a9a39a 35%, #d9d4cc 60%, #8ea3b5 85%, #b8c8d6 100%);
  }
  .front-panel-foot {
    left: 735px; top: 682px; width: 347px; height: 142px;
    background: linear-gradient(180deg, #444444 0%, #3a3a3a 100%);
  }
  .front-brand {
    left: 735px; top: 754px; width: 347px; text-align: center;
    font-size: 22px; font-weight: 700; letter-spacing: 1px; color: var(--mark-light);
  }
</style>
</head>
<body>
<main class="brochure">
  <div class="top-bar"></div>
  <div class="foot-band"></div>

  <!-- back panel -->
  <div class="banner" role="img" aria-label="Businessman in white shirt and tie lifting a dumbbell"></div>
  <p class="banner-kicker">Quartz Bridge Rehab</p>
  <p class="banner-title">CORPORATE FITNESS</p>
  <p class="banner-tag">maximize your company's profitability by improving<br>the overall fitness and health of your employees</p>

  <h2 class="pill pill-corporate">Corporate Fitness Services</h2>
  <p class="body-copy copy-corporate">Our team of experienced trainers and nutrition coaches will inspire your associates to transform their health and fitness, thus boosting your bottom line. We have fitness programming available all the way from the pinnacle of the company customizing solutions for your busy executives, (LeadTrim) to the core of the company by providing group exercise programs. Click here to learn more about our extraordinary Corporate Fitness Services.</p>
  <div class="photo-team" role="img" aria-label="Group fitness class exercising with barbells"></div>
  <p class="brand-name">QUARTZ BRIDGE REHAB</p>

  <ul class="service-list list-back">
    <li>Nutrition and Metabolic Detoxification Coaching</li>
    <li>Health Care Practitioner Grade Supplements</li>
    <li>Travel-Friendly Exercise Equipment</li>
    <li>In-Home Meal Catering</li>
  </ul>

  <!-- inside panel -->
  <h2 class="pill pill-leadtrim">Leadtrim</h2>
  <p class="body-copy copy-leadtrim">Research shows that 73% of Global 500 executives are underactive leading to 40% of them being obese. Add to that, 100% of the Global 500 executives studied had 1 risk factor for cardiovascular disease. As a solution to an increased waistline and decreased time and resources; QBR has tailored a fitness program that can match the demands and lifestyle specifically for executives. With QBR, business leaders can radically transform their fitness and health, leading to improvements in executive function. Research from the book “Ignite” shows that regular exercise for 12 weeks improves "executive function". Please click here to learn more about QBR's tailored program for corporate executives!</p>

  <section class="services-box">
    <h2 class="services-title">Leadtrim Services</h2>
    <p class="services-copy">One of the primary concerns of today’s business professional in relation to personal health is simply finding the time. We offer both on and off-site services to help remedy this issue for many executives. LeadTrim is fully customizable and our trainers and coaches are here to help you make healthy choices, even while out on the road; by doing accountability check-ins via VidLink, contacting the hotel you will be staying at to find out what kind of equipment they have on site to kout.</p>
    <div class="services-rule"></div>
  </section>

  <ul class="service-list list-inside">
    <li>On-Site Personal Training</li>
    <li>Off-Site Personal Training</li>
    <li>Far Infrared Sauna</li>
    <li>Off-Site suggested Menu</li>
  </ul>

  <!-- front panel -->
  <div class="logo-card"><span>QUARTZ BRIDGE<br>REHAB</span></div>
  <p class="story">Quartz Bridge Rehab began as a dream; the idea to combine all areas of health and fitness to give our clients the best possible fitness and nutritional experience. Marcus Hollen left Keystone Athletic Club, in Lake Harlow, MN, in the fall of 2004. His position as Personal Training Director left him frustrated; they wanted ideas on increasing revenue, not on how clients could get better results, or how to create the best atmosphere for trainers and clients to work. After much prayer, Marcus and Elena decided on the name Quartz Bridge Rehab, to reflect their deep belief that God is in charge of their lives and vocation.</p>
  <div class="photo-lift" role="img" aria-label="Close-up of an arm lifting a chrome dumbbell in a gym"></div>
  <div class="front-panel-foot"></div>
  <p class="front-brand">QUARTZ BRIDGE REHAB</p>

  <div class="foot-bar"></div>
</main>
</body>
</html>
```